Luxury Wine Label for New Startup Winery

We need a wine label for our new winery startup. We have worked with a local designer but do not feel the resulting label / logo have the elevation required to present our brand as a luxury wine. Our winery is called "Harrowgate Vineyards" and we are focused on extremely high quality hand crafted artisan and estate wines from the Pacific Northwest.
We would like to see designs that utilize a tree line, or other imagery that represents the "Harrowgate" part of our company name. Another interesting feature could be wood grain.
A logo will be required based on your design so please design with this in mind:
This logo should be consistent with the wine bottle label design, and should be representative of our high end exclusive wine while giving a sense of place (Oregon/ Pacific Northwest.)
I will supply an image of the design we received from our local designer, PLEASE NOTE: in general we do like wood grain and tree line concepts but feel the execution was poorly done.
ATTN: Logo design should be suitable for use on: Bottles (Red wine/rose/white wine), Bussiness cards, vehicle signage, business signage, etc
P.S.:
If you have a design that is not outside the box we are still interested in seeing it.
Label is for a burgundy style bottle with a label height of 3.5 - 4" and a width of 3.5-4"
any label <= 4"x4" and >=3.5"x3.5" will be acceptable:
HOWEVER Width should be greater than or equal to height due to the bottle format
Target Market(s)
Wine enthusiasts with adequate discretionary budgets to afford $100 bottles of wine.
Industry/Entity Type
Wine / Winery
Requirements
Must have
- A sense of luxury, a feel of exclusivity, and a theme consistent with our product and brand name
Nice to have
- Tree line, wood grain or other wood themes. Serif fonts
Should not have
- anything cheesy, off topic, hard to read script fonts or anything that makes the label hard to read from a few feet away or too busy

```html
<!DOCTYPE html>
<html lang="en">
<head>
<meta charset="utf-8">
<title>Harrowgate Vineyards – Syrah Label</title>
<link href="https://fonts.googleapis.com/css2?family=Italiana&family=Great+Vibes&family=Cormorant+Garamond:wght@700&family=Montserrat:wght@500&display=swap" rel="stylesheet">
<style>
  :root {
    --page: #ffffff;
    --label-black: #0b0b0b;
    --gold: #c99a4e;
    --gold-light: #e9c68a;
    --gold-pale: #f0d6a8;
    --gold-deep: #a86f2a;
    --wood: #5a2a0d;
    --frame-cream: #e6c596;
  }
  * { margin: 0; padding: 0; box-sizing: border-box; }
  html, body { width: 1200px; height: 1063px; overflow: hidden; background: var(--page); }
  .canvas { position: relative; width: 1200px; height: 1063px; }

  .main-label {
    position: absolute; left: 257px; top: 146px; width: 695px; height: 564px;
    background: var(--label-black);
  }
  .rule {
    position: absolute; left: 0; width: 100%; height: 3px;
    background: linear-gradient(90deg, #7a3d1c, var(--gold-light) 50%, #7a3d1c);
  }
  .rule--top { top: 76px; }
  .rule--bottom { top: 487px; }

  .brand-name {
    position: absolute; left: 0; width: 100%; top: 268px; text-align: center;
    font-weight: 400; line-height: 1;
  }
  .brand-name__main {
    display: block; font-family: "Italiana", serif; font-size: 86px; letter-spacing: 1px;
    color: var(--gold);
  }
  .brand-name__sub {
    display: block; font-family: "Montserrat", sans-serif; font-weight: 500;
    font-size: 21px; letter-spacing: 5px; margin-top: 10px; color: var(--gold-pale);
  }

  .region {
    position: absolute; left: 0; width: 100%; top: 414px; text-align: center;
    font-family: "Italiana", serif; font-size: 44px; letter-spacing: 3px; line-height: 1;
    background: linear-gradient(180deg, var(--gold-light), var(--gold-deep));
    -webkit-background-clip: text; background-clip: text; color: transparent;
  }

  .varietal-band {
    position: absolute; left: 254px; top: 779px; width: 697px; height: 142px;
    background: var(--wood);
  }
  .varietal-band__frame {
    position: absolute; inset: 8px 7px; border: 2px solid var(--frame-cream);
  }
  .varietal-name {
    position: absolute; left: 156px; top: -13px;
    padding: 30px 20px 30px 20px;
    font-family: "Great Vibes", cursive; font-weight: 400; font-size: 104px; line-height: 1;
    background: linear-gradient(180deg, var(--gold-light), var(--gold-deep));
    -webkit-background-clip: text; background-clip: text; color: transparent;
  }
  .vintage-line {
    position: absolute; left: 299px; top: 96px;
    font-family: "Cormorant Garamond", serif; font-weight: 700; font-size: 21px;
    color: var(--gold); letter-spacing: 0.3px; line-height: 1;
  }
</style>
</head>
<body>
<div class="canvas">
  <section class="main-label">
    <div class="rule rule--top"></div>
    <h1 class="brand-name">
      <span class="brand-name__main">Harrowgate</span>
      <span class="brand-name__sub">VINEYARDS</span>
    </h1>
    <p class="region">WILLAMETTE VALLEY</p>
    <div class="rule rule--bottom"></div>
  </section>

  <section class="varietal-band" role="img" aria-label="Wood grain band with varietal name">
    <div class="varietal-band__frame"></div>
    <h2 class="varietal-name">Syrah</h2>
    <p class="vintage-line">ESTATE | 2023 | GROWN</p>
  </section>
</div>
</body>
</html>
```